Not-for-profit Community Law Business Card

Not-for-Profit community law firm are looking for new business card design to accompany a new logo.
The cards are to assist the organisation in reaching their strategic objective of generating greater networking amongst the community; specifically with other service providers, clients, and community influencers.
It should stand out. Be professional, strong, creative, clear in detail. The logo should be a major feature of the design.
Updates

Hi All,

Thank you for the submissions so far. I have uploaded the logo and colour details again, as requested. If you have any further issues downloading them or need a different format please contact me on jess_harlow@bvm.net.au

Kind regards,

Industry/Entity Type

Law Firm

Requirements
Must have
• Logo (attached)
Person's name
Position
Phone
Fax
Email
PO Box address
Website
Colours from the logo.

```html
<!DOCTYPE html>
<html lang="en">
<head>
<meta charset="utf-8">
<title>Harbour Point Legal Centre – Business Card</title>
<link rel="stylesheet" href="https://fonts.googleapis.com/css2?family=Open+Sans:wght@400;600;700&family=Oswald:wght@500&display=swap">
<style>
  :root {
    --page-bg: #e9e7e3;
    --card-white: #f7f7f7;
    --card-shade: #e4e4e4;
    --brand-blue: #1677c0;
    --brand-navy: #253a8e;
    --ink: #2d2d2d;
    --rule: #6a6a6a;
    --on-blue: #ffffff;
  }
  * { box-sizing: border-box; margin: 0; padding: 0; }
  html, body { width: 1200px; height: 1200px; overflow: hidden; }
  body {
    background: var(--page-bg);
    font-family: "Open Sans", Arial, sans-serif;
    color: var(--ink);
    position: relative;
  }
  .card {
    position: absolute;
    left: 100px;
    width: 1000px;
    height: 560px;
    border-radius: 34px;
    overflow: hidden;
    box-shadow: 0 6px 18px rgba(0,0,0,0.18);
  }
  .card--front {
    top: 30px;
    background: radial-gradient(ellipse at 40% 45%, #ffffff 0%, var(--card-white) 45%, var(--card-shade) 100%);
  }
  .card--back {
    top: 610px;
    background: var(--brand-blue);
  }
  .side-band {
    position: absolute;
    width: 30px;
    background: var(--brand-navy);
  }
  .card--front .side-band--left  { left: 24px; top: 160px; height: 340px; }
  .card--front .side-band--right { right: 0; top: 60px; height: 270px; }
  .card--back .side-band--left   { left: 0; top: 110px; height: 340px; }
  .card--back .side-band--right  { right: 24px; top: 95px; height: 340px; }

  .brand-name {
    position: absolute;
    font-family: "Open Sans", Arial, sans-serif;
    font-weight: 600;
    font-variant: small-caps;
    letter-spacing: 1px;
    line-height: 1.05;
    display: flex;
    align-items: center;
  }
  .brand-name__dot {
    flex: none;
    border-radius: 50%;
  }
  .card--front .brand-name {
    left: 80px; top: 70px;
    color: var(--brand-blue);
    font-size: 34px;
    gap: 16px;
  }
  .card--front .brand-name__dot {
    width: 64px; height: 64px;
    background: var(--brand-blue);
  }
  .card--back .brand-name {
    left: 130px; top: 200px;
    color: var(--on-blue);
    font-size: 58px;
    gap: 28px;
  }
  .card--back .brand-name__dot {
    width: 130px; height: 130px;
    background: var(--on-blue);
  }
  .brand-name__sub { display: block; font-size: 0.62em; letter-spacing: 2px; }

  .divider {
    position: absolute;
    left: 560px; top: 190px;
    width: 1.5px; height: 260px;
    background: var(--rule);
  }
  .person {
    position: absolute;
    left: 250px; top: 380px;
    text-align: right;
  }
  .person__name {
    font-family: "Oswald", "Arial Narrow", sans-serif;
    font-weight: 500;
    font-size: 66px;
    line-height: 1;
    letter-spacing: -1px;
    color: var(--ink);
  }
  .person__role {
    font-size: 20px;
    margin-top: 6px;
    color: #444;
  }
  .contact {
    position: absolute;
    left: 595px; top: 200px;
    list-style: none;
    font-size: 17px;
    color: #333;
  }
  .contact__item {
    display: flex;
    align-items: center;
    gap: 14px;
    margin-bottom: 12px;
  }
  .contact__item--address { margin-bottom: 36px; align-items: flex-start; }
  .contact__icon {
    flex: none;
    width: 28px; height: 28px;
    border-radius: 6px;
    background: var(--brand-blue);
    display: flex; align-items: center; justify-content: center;
  }
  .contact__icon svg { width: 18px; height: 18px; }
</style>
</head>
<body>

<section class="card card--front" aria-label="Business card front">
  <div class="side-band side-band--left"></div>
  <div class="side-band side-band--right"></div>

  <div class="brand-name">
    <span class="brand-name__dot"></span>
    <span>Harbour Point<span class="brand-name__sub">Legal Centre Inc.</span></span>
  </div>

  <div class="person">
    <p class="person__name">Mara Quinn</p>
    <p class="person__role">Managing Director</p>
  </div>

  <div class="divider"></div>

  <ul class="contact">
    <li class="contact__item contact__item--address">
      <span class="contact__icon"><svg viewBox="0 0 24 24"><path fill="#fff" d="M12 2a7 7 0 0 0-7 7c0 5 7 13 7 13s7-8 7-13a7 7 0 0 0-7-7zm0 9.5A2.5 2.5 0 1 1 12 6.5a2.5 2.5 0 0 1 0 5z"/></svg></span>
      <span>Suspendisse et massa in orci<br>porttitor adipiscing</span>
    </li>
    <li class="contact__item">
      <span class="contact__icon"><svg viewBox="0 0 24 24"><path fill="#fff" d="M3 9c0-2 4-4 9-4s9 2 9 4v2h-5V9H8v2H3zM6 12h12l2 8H4z"/></svg></span>
      <span>+123 456 7890</span>
    </li>
    <li class="contact__item">
      <span class="contact__icon"><svg viewBox="0 0 24 24"><rect x="7" y="2" width="10" height="20" rx="2" fill="#fff"/><rect x="9" y="5" width="6" height="8" fill="#1677c0"/></svg></span>
      <span>+123 456 7890</span>
    </li>
    <li class="contact__item">
      <span class="contact__icon"><svg viewBox="0 0 24 24"><rect x="3" y="6" width="18" height="12" rx="1" fill="#fff"/><path d="M3 6l9 7 9-7" fill="none" stroke="#1677c0" stroke-width="1.6"/></svg></span>
      <span>mara@harbourpointlegal.org</span>
    </li>
    <li class="contact__item">
      <span class="contact__icon"><svg viewBox="0 0 24 24" fill="none" stroke="#fff" stroke-width="1.6"><circle cx="12" cy="12" r="9"/><path d="M3 12h18M12 3c3 3 3 15 0 18M12 3c-3 3-3 15 0 18"/></svg></span>
      <span>www.harbourpointlegal.org</span>
    </li>
  </ul>
</section>

<section class="card card--back" aria-label="Business card back">
  <div class="side-band side-band--left"></div>
  <div class="side-band side-band--right"></div>

  <div class="brand-name">
    <span class="brand-name__dot"></span>
    <span>Harbour Point<span class="brand-name__sub">Legal Centre Inc.</span></span>
  </div>
</section>

</body>
</html>
```